New Stationary Design

Harlow Voltworks Ltd have acquired Brackmoor Kitchen Supply Ltd. We will be retaining the Brackmoor Kitchen Supply Ltd name and require new letter head, compliment slips & business card designs.

I have attached the existing Harlow Voltworks letterhead to show our current image/brand. I do not wish to change this substantially & imagine maybe a swap of colours from Red logo to Blue, and the title & footer bars maybe in Red. That said, I'm open to subtle changes in the overall design & to maybe modernise it and if we like them, we would probably ask the Designer to update the changes to reflect them on the Harlow Voltworks stationary as well.

We will be able to get some proper high def images for Catering equipment to include, but for the time being if desingers can use any standard stock images for initial presentation.

The logo will be printed onto a Red van so somehow we need to be able to modify it for that use.

Brackmoor Kitchen Supply Ltd. Correspondence Address: 47 Lower Fenwick Road, Northampton. NN3 8QX. Tel 01604 738 092. Fax 01604 738 416. No website currently. Registered No: 05817264. Vat No: 418 3052 96. Company Registered Address: 22 Calloway Close, Leicester. LE2 7RN. We would also like to mention that we have Regional Service Centres also based in Leicester & Stockport.

Business Cards would be for;

Owen Pritchard, Director. owen.pritchard@brackmoorkitchensupply.co.uk

Trevor Holbrook, Operations Manager. trevor.holbrook@brackmoorkitchensupply.co.uk

Neil Dunmore, Service Manager. neil.dunmore@brackmoorkitchensupply.co.uk

Simon Ketley, Business Development Manager. simon.ketley@brackmoorkitchensupply.co.uk

We would also like the letter head to include the 'Flue Sure' logo & our registration Number: To be confirmed. Also the Electrical Contractors logo & the words Wiring Trades Guild underneath so people know what it means. See www.wtgx.co.uk

Target Market(s)

Businesses who use Catering Equipment such as Cookers. fridges etc. Hence, Care Homes, Hospitals, Restaurants etc

Industry/Entity Type

Business

Requirements
Must have
• Resemblance to existing Harlow Voltworks brand, although maybe with some changes & modernisation.
Nice to have
• Could maybe have some 'icons' for the type of equipment we sell instead of photos. Ie Cookers, Ovens, Fridges, Microwaves, Dishwashers, as well as kithen cateringtabling, commercial extraction hoods etc.

```html
<!DOCTYPE html>
<html lang="en">
<head>
<meta charset="utf-8">
<title>Brackmoor Kitchen Supply – Stationery</title>
<link href="https://fonts.googleapis.com/css2?family=Barlow:wght@400;500;700&display=swap" rel="stylesheet">
<style>
  :root{
    --blue:#1b7fd0;
    --blue-deep:#0f5fae;
    --blue-light:#4aa8ea;
    --paper:#ffffff;
    --board:#f4f4f4;
    --ink:#333333;
    --rule:#cfe6f8;
    --silver-1:#f6f6f6;
    --silver-2:#bfc2c6;
    --badge-yellow:#f2d21a;
    --badge-grey:#e9e9e9;
  }
  *{box-sizing:border-box;margin:0;padding:0}
  html,body{width:1200px;height:900px;overflow:hidden}
  body{
    background:radial-gradient(ellipse at 50% 40%,#ffffff 0%,var(--board) 100%);
    font-family:"Barlow",Arial,sans-serif;color:var(--ink);position:relative;
  }
  .section-label{position:absolute;font-size:14px;color:#222}

  /* brand mark */
  .brand-mark{
    position:absolute;background:var(--blue);border:2px solid #fff;border-radius:6px;
    box-shadow:0 2px 4px rgba(0,0,0,.25);
    display:flex;align-items:center;justify-content:center;text-align:center;
    color:#fff;font-weight:700;line-height:1.05;
  }

  /* letterhead */
  .letterhead{position:absolute;left:40px;top:36px;width:452px;height:620px;background:var(--paper);
    box-shadow:0 1px 4px rgba(0,0,0,.25);overflow:hidden}
  .letterhead .header-wash{position:absolute;left:0;top:0;width:100%;height:70px;
    background:linear-gradient(90deg,rgba(27,127,208,.15),rgba(27,127,208,.05) 60%,rgba(255,255,255,0))}
  .footer-band{position:absolute;left:0;bottom:0;width:100%;
    background:linear-gradient(90deg,var(--blue-deep),var(--blue) 60%,var(--blue-light));
    color:#fff;font-size:5.5px;line-height:1.35;display:flex;align-items:center;padding:0 10px;gap:24px}
  .letterhead .footer-band{height:56px}
  .footer-band .badges{margin-left:auto;display:flex;gap:4px;align-items:flex-end}
  .badge-plain{background:var(--badge-grey);width:30px;height:22px}
  .badge-square{background:var(--badge-yellow);width:14px;height:14px}

  /* compliment slip */
  .comp-slip{position:absolute;left:504px;top:36px;width:446px;height:188px;background:var(--paper);
    box-shadow:0 1px 4px rgba(0,0,0,.25);overflow:hidden}
  .comp-slip .header-wash{position:absolute;left:0;top:0;width:100%;height:60px;
    background:linear-gradient(90deg,rgba(27,127,208,.15),rgba(255,255,255,0) 70%)}
  .comp-slip .footer-band{height:54px}
  .with-compliments{position:absolute;right:12px;bottom:60px;font-size:11px;color:var(--blue)}
  .slip-rule{position:absolute;right:0;bottom:56px;width:160px;border-top:1px solid var(--blue)}
  .comp-slip .slip-edge{position:absolute;right:0;bottom:54px;width:2px;height:70px;background:var(--blue)}

  /* business card back */
  .card-back{position:absolute;width:310px;height:200px;
    background:linear-gradient(160deg,var(--blue-light) 0%,var(--blue) 45%,var(--blue-deep) 100%);
    clip-path:polygon(0 0,93% 0,100% 8%,100% 100%,0 100%);color:#fff}
  .card-back .top-strip{position:absolute;left:8px;top:6px;width:180px;height:10px;background:#e7eef5}
  .card-back .brand-mark{right:14px;top:18px;width:88px;height:44px;font-size:11px}
  .card-back .person-name{position:absolute;left:18px;top:86px;font-size:23px;font-weight:700}
  .card-back .name-rule{position:absolute;left:18px;top:118px;width:180px;border-top:1.5px solid rgba(255,255,255,.8)}
  .card-back .job-title{position:absolute;left:18px;top:124px;font-size:15px;font-weight:400;color:#dbefff}
  .card-back .email-rule{position:absolute;left:18px;right:12px;top:170px;border-top:1px solid rgba(255,255,255,.8)}
  .card-back .email{position:absolute;right:14px;top:174px;font-size:11px}

  /* business card front */
  .card-front{position:absolute;left:170px;top:680px;width:330px;height:200px;
    background:linear-gradient(100deg,var(--silver-1) 0%,#e3e4e6 40%,var(--silver-2) 100%);
    box-shadow:0 1px 4px rgba(0,0,0,.2)}
  .card-front .bracket{position:absolute;left:10px;top:10px;width:140px;height:180px;
    border:2px solid var(--blue);border-right:none}
  .card-front .contact{position:absolute;left:18px;top:18px;font-size:7.5px;line-height:1.45;color:var(--blue-deep)}
  .card-front .contact p + p{margin-top:8px}
  .card-front .brand-mark{right:14px;top:74px;width:130px;height:62px;font-size:15px}
</style>
</head>
<body>

<span class="section-label" style="left:16px;top:6px">letterhead</span>
<span class="section-label" style="left:504px;top:4px">compliment slips</span>
<span class="section-label" style="left:994px;top:4px">logo</span>
<span class="section-label" style="left:516px;top:380px">bc/back</span>
<span class="section-label" style="left:84px;top:852px">bc/front</span>

<!-- letterhead -->
<section class="letterhead">
  <div class="header-wash"></div>
  <div class="brand-mark" style="left:16px;top:18px;width:110px;height:48px;font-size:12px">Brackmoor<br>Kitchen Supply</div>
  <footer class="footer-band">
    <div>Brackmoor Kitchen Supply Ltd<br>Correspondence Address: 47 Lower Fenwick Road,<br>Northampton. NN3 8QX<br>Tel 01604 738 092 Fax 01604 738 416</div>
    <div>Registered No: 05817264 Vat No: 418 3052 96<br>Company Registered Address: 22 Calloway Close,<br>Leicester. LE2 7RN</div>
    <div class="badges"><span class="badge-plain"></span><span class="badge-square"></span></div>
  </footer>
</section>

<!-- compliment slip -->
<section class="comp-slip">
  <div class="header-wash"></div>
  <div class="brand-mark" style="left:14px;top:12px;width:104px;height:44px;font-size:11px">Brackmoor<br>Kitchen Supply</div>
  <span class="slip-edge"></span>
  <span class="slip-rule"></span>
  <span class="with-compliments">with compliments</span>
  <footer class="footer-band">
    <div>Brackmoor Kitchen Supply Ltd<br>Correspondence Address: 47 Lower Fenwick Road,<br>Northampton. NN3 8QX<br>Tel 01604 738 092 Fax 01604 738 416</div>
    <div>Registered No: 05817264 Vat No: 418 3052 96<br>Company Registered Address: 22 Calloway Close,<br>Leicester. LE2 7RN</div>
    <div class="badges"><span class="badge-plain"></span><span class="badge-square"></span></div>
  </footer>
</section>

<!-- logo -->
<div class="brand-mark" style="left:994px;top:36px;width:176px;height:92px;font-size:21px">Brackmoor<br>Kitchen Supply</div>

<!-- business card backs -->
<article class="card-back" style="left:516px;top:420px">
  <span class="top-strip"></span>
  <div class="brand-mark">Brackmoor<br>Kitchen Supply</div>
  <h2 class="person-name">Owen Pritchard</h2>
  <span class="name-rule"></span>
  <p class="job-title">Director</p>
  <span class="email-rule"></span>
  <p class="email">owen.pritchard@brackmoorkitchensupply.co.uk</p>
</article>

<article class="card-back" style="left:844px;top:420px">
  <span class="top-strip"></span>
  <div class="brand-mark">Brackmoor<br>Kitchen Supply</div>
  <h2 class="person-name">Neil Dunmore</h2>
  <span class="name-rule"></span>
  <p class="job-title">Service Manager</p>
  <span class="email-rule"></span>
  <p class="email">neil.dunmore@brackmoorkitchensupply.co.uk</p>
</article>

<article class="card-back" style="left:516px;top:674px">
  <span class="top-strip"></span>
  <div class="brand-mark">Brackmoor<br>Kitchen Supply</div>
  <h2 class="person-name">Trevor Holbrook</h2>
  <span class="name-rule"></span>
  <p class="job-title">Operations Manager</p>
  <span class="email-rule"></span>
  <p class="email">trevor.holbrook@brackmoorkitchensupply.co.uk</p>
</article>

<article class="card-back" style="left:844px;top:674px">
  <span class="top-strip"></span>
  <div class="brand-mark">Brackmoor<br>Kitchen Supply</div>
  <h2 class="person-name">Simon Ketley</h2>
  <span class="name-rule"></span>
  <p class="job-title">Business Development Manager</p>
  <span class="email-rule"></span>
  <p class="email">simon.ketley@brackmoorkitchensupply.co.uk</p>
</article>

<!-- business card front -->
<article class="card-front">
  <span class="bracket"></span>
  <div class="contact">
    <p>Brackmoor Kitchen Supply Ltd<br>Correspondence Address:<br>47 Lower Fenwick Road,<br>Northampton. NN3 8QX<br>Tel 01604 738 092<br>Fax 01604 738 416</p>
    <p>Registered No: 05817264<br>Vat No: 418 3052 96<br>Company Registered Address:<br>22 Calloway Close,<br>Leicester. LE2 7RN</p>
  </div>
  <div class="brand-mark">Brackmoor<br>Kitchen Supply</div>
</article>

</body>
</html>
```